DuneOrbit Signage Design Project

We need a signage design for our company's new location, we are a GPS tracking and monitoring systems company,

we would like to see signage designs that use colors similar to the company's logo,

Please consider that we will add Arabic words in all Signage,

new photos uploaded...

Target Market(s)

GPS/GPRS tracking and monitoring systems

Industry/Entity Type

Gps

Requirements
Must have
• Large billboard must have out-frame details and some idea related to tracking and navigation systems. (similar to the attached Photo)

1- We need billboard signage,
2- outdoor signage and on-glass signage
3- garage signage,

Nice to have
• logo attached, earth, satellite, location pin, map.

```html
<!DOCTYPE html>
<html lang="en">
<head>
<meta charset="utf-8">
<title>DuneOrbit – New Location Billboard</title>
<link rel="stylesheet" href="https://fonts.googleapis.com/css2?family=Archivo:ital,wght@0,800;1,900&display=swap">
<style>
  :root {
    --backdrop: #eceef0;
    --board: #ffffff;
    --board-edge: #d4d6d8;
    --ink: #1c1b1c;
    --signal-red: #ec1c24;
  }
  * { margin: 0; padding: 0; box-sizing: border-box; }
  html, body {
    width: 1200px;
    height: 1000px;
    overflow: hidden;
    background: var(--backdrop);
  }
  .canvas {
    position: relative;
    width: 1200px;
    height: 1000px;
  }
  .billboard-face {
    position: absolute;
    left: 55px;
    top: 112px;
    width: 1090px;
    height: 528px;
    background: var(--board);
    border: 2px solid var(--board-edge);
  }
  .signal-waves {
    position: absolute;
    left: 0;
    top: 0;
  }
  .headline {
    position: absolute;
    left: 0;
    top: 162px;
    width: 1090px;
    text-align: center;
    font-family: "Archivo", "Arial Black", sans-serif;
    font-style: italic;
    font-weight: 900;
    font-size: 82px;
    line-height: 88px;
    color: var(--ink);
    letter-spacing: 1px;
  }
  .address {
    position: absolute;
    left: 210px;
    top: 412px;
    font-family: "Archivo", "Arial Black", sans-serif;
    font-weight: 800;
    font-size: 40px;
    color: var(--ink);
    letter-spacing: 0.5px;
  }
  .brand {
    position: absolute;
    left: 712px;
    top: 404px;
    display: flex;
    align-items: center;
    gap: 14px;
  }
  .brand-dot {
    width: 40px;
    height: 40px;
    border-radius: 50%;
    background: var(--signal-red);
  }
  .brand-name {
    font-family: "Archivo", "Arial Black", sans-serif;
    font-weight: 800;
    font-size: 48px;
    color: var(--ink);
  }
</style>
</head>
<body>
  <main class="canvas">
    <section class="billboard-face">
      <svg class="signal-waves" width="300" height="260" viewBox="55 112 300 260" aria-hidden="true">
        <g fill="none" stroke="var(--signal-red)" stroke-width="17" stroke-linecap="round">
          <path d="M 240 153 A 165 165 0 0 0 82 290"/>
          <path d="M 242 195 A 125 125 0 0 0 124 298"/>
          <path d="M 248 240 A 80 80 0 0 0 168 310"/>
        </g>
      </svg>
      <h1 class="headline">Dune Orbit has<br>a new location</h1>
      <p class="address">123 Dune Avenue</p>
      <div class="brand">
        <span class="brand-dot"></span>
        <span class="brand-name">DuneOrbit</span>
      </div>
    </section>
  </main>
</body>
</html>
```